Plate Rally! Digital Order Web App

This is a web app on mobile phone, for consumers to order food inside a restaurant using their phones. we have done up the flow but we need to revamp UI design. pls have a look at our current web on your mobile phone:
https://demo.tavrozi.app/o/KLMV/314725

CURRENT DESIGN.
1. food category on left side, always shown. menu items in list view with image.
2. when we click on an item, there is popup page, to select modifiers, or quantity.
3. order review page(cart page) is quite messy now, need a complete new look.
4 payment page(no need to design, handle by Quellon)
5. order confirmation page. success or error return

DESIGN requirements:
please browse through and click to order with current page above. we have put in lots of thoughts and effort for current flow, the new design should base on this flow.
1. web app. no zoom in/out is allowed for users. responsive html to suit different mobile phone screen size. modern fonts.
2. PAGES needed:
home/welcome page,
well laid out menu items page,
single item page, with add on choice and modifier
cart page(to include recommended items, ordered item list, remove item total, changeable quantity,
confirmation page(success, fail)

DELIVERABLES - responsive html, fonts, images asset such as icons, animation, button images(suitable for commercial use without further third party loyalty fee)
Updates

Hi all if we have left a comment on ur design, please revise accordingly and we will conclude it soon!

Target Market(s)

young diners who order food on their mobile phone.

Industry/Entity Type

Restaurant

Coding

Coded - Design and coding required

Number of Pages Required

5+ page

Colors

Designer to choose colors to be used in the design.

Requirements
Must have
• - lively, appetising colors while making the page easy to read. easy on eyes.
• - consistency. fonts used.
Nice to have
• - 2 color schemes
• - html codes. we will top up if you can deliver coded html.
Should not have
• - should not have more than 3 colors
• - should not have more than 3 different fonts
• - should not use colors that are dull

```html
<!DOCTYPE html>
<html lang="en">
<head>
<meta charset="utf-8">
<title>tavrozi — Order App Screens</title>
<link href="https://fonts.googleapis.com/css2?family=Roboto:wght@300;400;500;700&display=swap" rel="stylesheet">
<style>
:root{
  --magenta:#d4007a;
  --teal:#66c7c7;
  --teal-dark:#55b5b6;
  --ink:#1b1b1b;
  --footer:#121c26;
  --stage:#e6e6e6;
  --pale:#eef6fa;
  --line:#cfe3ea;
}
*{box-sizing:border-box;margin:0;padding:0}
html,body{width:1200px;height:781px;overflow:hidden}
body{background:var(--stage);font-family:"Roboto",Arial,sans-serif;color:var(--ink);position:relative}
.screen{position:absolute;width:290px;height:624px;border-radius:22px;overflow:hidden;background:#fff}
.screen *{position:absolute}
.screen-home{left:71px;top:50px}
.screen-menu{left:443px;top:55px;background:linear-gradient(#f7fbfd,var(--pale))}
.screen-cart{left:821px;top:50px;background:linear-gradient(#f7fbfd,var(--pale))}
.brand{font-weight:500;font-size:26px;color:#fff;letter-spacing:.5px}
.burger{width:31px;height:17px;border-top:2px solid #fff;border-bottom:2px solid #fff}
.burger::after{content:"";position:absolute;left:0;right:0;top:5.5px;border-top:2px solid #fff}
.footer{left:0;right:0;bottom:0;height:45px;background:var(--footer);color:#eef;font-size:13px;font-weight:300;display:flex;align-items:center;justify-content:center}
.footer *{position:static}

/* home */
.hero-photo{left:0;top:0;width:290px;height:372px;background:radial-gradient(ellipse at 40% 40%,#6a3a22,#3a1d12 60%,#24120b)}
.hero-curve{left:0;top:340px}
.home .brand{left:120px;top:82px}
.headline{left:0;width:276px;top:112px;text-align:center;color:#fff;font-weight:700;font-size:24px;line-height:30px}
.lede{left:0;width:276px;top:184px;text-align:center;color:#fff;font-size:11.5px;line-height:17px;font-weight:300}
.search-field{left:28px;top:233px;width:245px;height:36px;background:#fff;font-size:13px;color:#555;display:flex;align-items:center;padding-left:30px}
.search-field svg{left:9px;top:10px}
.btn-search{left:28px;top:279px;width:245px;height:36px;background:var(--magenta);color:#fff;font-weight:700;font-size:17px;display:flex;align-items:center;justify-content:center}
.feature-icon{left:30px;width:55px;height:55px;border-radius:50%;background:var(--teal)}
.feature-title{left:97px;color:var(--magenta);font-weight:700;font-size:15px}
.feature-text{left:97px;font-size:11.5px;font-weight:300}

/* menu */
.header{left:0;top:0;width:290px;height:81px;background:linear-gradient(#72d0d0,var(--teal-dark))}
.screen-menu .brand,.screen-cart .brand{left:86px;top:30px}
.category-bar{left:11px;top:88px;width:268px;height:36px;background:var(--magenta);color:#fff;font-weight:700;font-size:15.5px;display:flex;align-items:center;justify-content:center}
.category-bar::after{content:"";position:absolute;left:127px;bottom:-7px;border:7px solid transparent;border-bottom:0;border-top-color:var(--magenta)}
.categories{left:9px;top:152px;list-style:none}
.categories li{position:static;font-size:12px;height:30px;font-weight:300;color:#222}
.categories .active{color:var(--magenta);font-weight:700}
.dish-card{left:80px;width:199px;height:79px;background:#fff;border:1px solid #dde8ee}
.dish-photo{left:0;top:0;width:89px;height:77px}
.dish-name{left:105px;top:8px;font-size:11.5px;font-weight:700;line-height:13px;color:#333}
.dish-price{left:105px;top:54px;font-size:9.5px;font-weight:700;color:var(--magenta)}
.add-tab{right:-1px;top:18px}

/* cart */
.timeline{left:38px;top:112px;width:4px;height:386px;background:var(--teal)}
.step{left:29px;width:22px;height:22px;border-radius:50%;background:var(--magenta)}
.step::after{content:"";position:absolute;left:7px;top:7px;width:8px;height:8px;border-radius:50%;background:#fff}
.step-first{box-shadow:0 0 0 3px #fff,0 0 0 5px var(--teal)}
.step-title{left:65px;font-size:15px;font-weight:700}
.qty{left:66px;width:44px;height:22px;border:1px solid #ccc;background:#fff;font-size:11px;display:flex;justify-content:space-between;align-items:center;padding:0 4px}
.qty *{position:static}
.qty .sign{color:var(--magenta)}
.line-item{left:120px;font-size:10px;font-weight:700}
.remove-all{right:20px;top:190px;font-size:8.5px;text-decoration:underline;color:#333}
.subhead{left:65px;font-size:11px;font-weight:700}
.rec{top:236px;width:62px;height:48px}
.rec span{left:6px;bottom:3px;color:#fff;font-size:8.5px;font-weight:700}
.label{left:66px;font-size:11px;font-weight:300}
.field{left:66px;width:206px;background:#fff;border:1px solid #b9dde3}
.subtotal{right:24px;top:361px;font-size:13px;font-weight:700;color:var(--magenta)}
.btn{top:515px;width:80px;height:39px;color:#fff;font-size:10px;font-weight:700;text-align:center;line-height:12px;display:flex;align-items:center;justify-content:center}
.btn-pay{left:65px;background:var(--magenta)}
.btn-add{left:155px;background:var(--teal)}
</style>
</head>
<body>

<section class="screen screen-home home">
  <div class="hero-photo" role="img" aria-label="Dark close-up photo of grilled skewered food"></div>
  <svg class="hero-curve" width="290" height="40" viewBox="0 0 290 40"><path d="M0 40 L0 28 Q145 -16 290 28 L290 40 Z" fill="#fff"/></svg>
  <div class="brand">tavrozi</div>
  <div class="burger" style="left:233px;top:44px"></div>
  <h1 class="headline">Order Great Food<br>on Great Price</h1>
  <p class="lede">Lorem ipsum dolor sit amet consectetuer<br>adipiscing elit Nam cursus Morbi ut</p>
  <div class="search-field">
    <svg width="16" height="16" viewBox="0 0 16 16"><circle cx="6.5" cy="6.5" r="5" fill="none" stroke="#888" stroke-width="2"/><line x1="10" y1="10" x2="15" y2="15" stroke="#888" stroke-width="2"/></svg>
    Search Your Dish
  </div>
  <div class="btn-search">Search</div>

  <div class="feature-icon" style="top:373px"><svg width="55" height="55" viewBox="0 0 55 55"><circle cx="27.5" cy="27.5" r="15" fill="none" stroke="#fff" stroke-width="2"/><path d="M21 28 l5 5 l9 -10" fill="none" stroke="#fff" stroke-width="2"/></svg></div>
  <div class="feature-title" style="top:384px">No Minimum Order</div>
  <div class="feature-text" style="top:405px">Lorem ipsum dolor sit amet co</div>

  <div class="feature-icon" style="top:441px"><svg width="55" height="55" viewBox="0 0 55 55" fill="none" stroke="#fff" stroke-width="2"><circle cx="35" cy="18" r="5"/><circle cx="19" cy="31" r="4"/><path d="M35 24 v4 q0 4 -4 4 h-4 q-4 0 -4 4 t4 4 h12"/><path d="M19 36 v4"/></svg></div>
  <div class="feature-title" style="top:452px">Live Tracking</div>
  <div class="feature-text" style="top:472px">Lorem ipsum dolor sit amet co</div>

  <div class="feature-icon" style="top:508px"><svg width="55" height="55" viewBox="0 0 55 55" fill="none" stroke="#fff" stroke-width="2"><path d="M13 33 q0 -15 14.5 -15 q14.5 0 14.5 15 z"/><line x1="10" y1="37" x2="45" y2="37"/><circle cx="27.5" cy="16" r="2"/></svg></div>
  <div class="feature-title" style="top:519px">Top Quality Food</div>
  <div class="feature-text" style="top:539px">Lorem ipsum dolor sit amet co</div>

  <footer class="footer">© 2019 Company Name</footer>
</section>

<section class="screen screen-menu">
  <div class="header"></div>
  <div class="brand">tavrozi</div>
  <div class="burger" style="left:234px;top:44px"></div>
  <div class="category-bar">Vegetables</div>
  <ul class="categories">
    <li class="active">Vegetable</li><li>Meat</li><li>Seafood</li><li>Special</li><li>Cold Dish</li><li>Main</li><li>Set</li><li>Juice</li><li>Drink</li><li>Beer</li><li>Alcohol</li><li>Wine</li>
  </ul>

  <div class="dish-card" style="top:143px">
    <div class="dish-photo" role="img" aria-label="Photo of grilled golden buns" style="background:linear-gradient(135deg,#6b4a2a,#e0a14a 50%,#8a5a2a)"></div>
    <div class="dish-name">Grilled<br>Mutton Bbq<br>烤羊肉串</div><div class="dish-price">$1.00</div>
    <svg class="add-tab" width="16" height="42" viewBox="0 0 16 42"><path d="M16 0 L16 42 L4 30 L0 21 L4 12 Z" fill="#66c7c7"/><path d="M9 17 v8 M5 21 h8" stroke="#fff" stroke-width="2"/></svg>
  </div>
  <div class="dish-card" style="top:230px">
    <div class="dish-photo" role="img" aria-label="Photo of grilled lettuce skewers" style="background:linear-gradient(135deg,#5d8a3a,#b9d98a 50%,#6e9b45)"></div>
    <div class="dish-name">Grilled<br>Mutton Bbq<br>烤羊肉串</div><div class="dish-price">$1.00</div>
    <svg class="add-tab" width="16" height="42" viewBox="0 0 16 42"><path d="M16 0 L16 42 L4 30 L0 21 L4 12 Z" fill="#66c7c7"/><path d="M9 17 v8 M5 21 h8" stroke="#fff" stroke-width="2"/></svg>
  </div>
  <div class="dish-card" style="top:317px">
    <div class="dish-photo" role="img" aria-label="Photo of grilled meat and mushroom skewers" style="background:linear-gradient(135deg,#3a2414,#a5602a 50%,#4a2c18)"></div>
    <div class="dish-name">Grilled<br>Mutton Bbq<br>烤羊肉串</div><div class="dish-price">$1.00</div>
    <svg class="add-tab" width="16" height="42" viewBox="0 0 16 42"><path d="M16 0 L16 42 L4 30 L0 21 L4 12 Z" fill="#66c7c7"/><path d="M9 17 v8 M5 21 h8" stroke="#fff" stroke-width="2"/></svg>
  </div>
  <div class="dish-card" style="top:404px">
    <div class="dish-photo" role="img" aria-label="Photo of grilled green bean skewers" style="background:linear-gradient(135deg,#4a3020,#3f9a2a 45%,#2f7a22)"></div>
    <div class="dish-name">Grilled<br>Mutton Bbq<br>烤羊肉串</div><div class="dish-price">$1.00</div>
    <svg class="add-tab" width="16" height="42" viewBox="0 0 16 42"><path d="M16 0 L16 42 L4 30 L0 21 L4 12 Z" fill="#66c7c7"/><path d="M9 17 v8 M5 21 h8" stroke="#fff" stroke-width="2"/></svg>
  </div>
  <div class="dish-card" style="top:491px">
    <div class="dish-photo" role="img" aria-label="Photo of grilled potato skewers" style="background:linear-gradient(135deg,#6a3a1a,#e6b23a 50%,#9a5a1a)"></div>
    <div class="dish-name">Grilled<br>Mutton Bbq<br>烤羊肉串</div><div class="dish-price">$1.00</div>
    <svg class="add-tab" width="16" height="42" viewBox="0 0 16 42"><path d="M16 0 L16 42 L4 30 L0 21 L4 12 Z" fill="#66c7c7"/><path d="M9 17 v8 M5 21 h8" stroke="#fff" stroke-width="2"/></svg>
  </div>

  <footer class="footer">© 2019 Company Name</footer>
</section>

<section class="screen screen-cart">
  <div class="header"></div>
  <div class="brand">tavrozi</div>
  <div class="burger" style="left:234px;top:43px"></div>

  <div class="timeline"></div>
  <div class="step step-first" style="top:101px"></div>
  <div class="step" style="top:388px"></div>
  <div class="step" style="top:486px"></div>

  <h2 class="step-title" style="top:96px">Review Your Order</h2>
  <div class="qty" style="top:124px"><span class="sign">–</span><span>1</span><span class="sign">+</span></div>
  <div class="line-item" style="top:130px">Homemade Plum Juice Glass</div>
  <div class="qty" style="top:158px"><span class="sign">–</span><span>1</span><span class="sign">+</span></div>
  <div class="line-item" style="top:164px">Spicy Marinated Crayfish</div>
  <div class="remove-all">Remove all items</div>

  <div class="subhead" style="top:215px">Recommended items</div>
  <div class="rec" style="left:66px" role="img" aria-label="Photo of grilled vegetable skewers" ><div style="inset:0;background:linear-gradient(135deg,#3f6a2a,#9cc46a)"></div><span>Dish Title</span></div>
  <div class="rec" style="left:138px" role="img" aria-label="Photo of grilled meat skewers"><div style="inset:0;background:linear-gradient(135deg,#3a2414,#b0682a)"></div><span>Dish Title</span></div>
  <div class="rec" style="left:212px" role="img" aria-label="Photo of grilled potato skewers"><div style="inset:0;background:linear-gradient(135deg,#7a3a14,#e0a83a)"></div><span>Dish Title</span></div>

  <div class="label" style="top:309px">Remarks for all itmes:</div>
  <div class="field" style="top:327px;height:26px"></div>
  <div class="label" style="top:362px">Subtotal</div>
  <div class="subtotal">$ 15.60</div>

  <h2 class="step-title" style="top:391px">Key in Mobile No.</h2>
  <div class="label" style="top:419px">To Enjoy Member Benefits</div>
  <div class="field" style="top:438px;height:30px"></div>

  <h2 class="step-title" style="top:489px">Select a Payment</h2>
  <div class="btn btn-pay">Pay with<br>Credit Card</div>
  <div class="btn btn-add">Add Other<br>Items</div>

  <footer class="footer">© 2019 Company Name</footer>
</section>

</body>
</html>
```